Wanderlark Gin - Bottle Label for a craft Gin about to be launched on the world from New Zealand

We are a start up craft distillery in New Zealand. We have developed a wonderful Gin using our own grain spirit and both traditional and New Zealand native botanicals (Manuka to be specific), chosen our bottle and the name "Wanderlark" and done a bit of amateur label design and now we are looking for someone to make it great.

Feel free to change up our amateur concept but give us something that will pop from the back bar and scream authenticity, craft and individuality.

The attached files give you the specifications of the bottle, our current concept for a Wanderlark label and an earlier concept drawing that gives an idea of where we are thinking the two labels should go on the front of the bottle.

Thanks, we look forward to your ideas!!

Target Market(s)

High end and craft Gin drinkers. Hipsters and cocktail barflys and their bar tenders and bar owners

Requirements
Must have
• Attractive individuality
Nice to have
• Coolness
Should not have
• Uncoolness

```html
<!DOCTYPE html>
<html lang="en">
<head>
<meta charset="utf-8">
<title>Wanderlark Small Batch Gin – Labels</title>
<link rel="stylesheet" href="https://fonts.googleapis.com/css2?family=Great+Vibes&family=Cinzel:wght@600&family=Oswald:wght@500&family=Pompiere&family=Arimo&family=Cormorant+Garamond:wght@500&display=swap">
<style>
  :root {
    --bg-top: #2b5a58;
    --bg-bottom: #163769;
    --sage: #8fae98;
    --sage-deep: #5f8a6b;
    --sage-text: #7e9f88;
    --paper: #ffffff;
    --ink: #141414;
    --filigree: 190, 190, 190;
    --filigree-green: 88, 132, 100;
    --emblem: #1c1c1c;
  }
  * { margin: 0; padding: 0; box-sizing: border-box; }
  html, body { width: 1200px; height: 1200px; overflow: hidden; }
  body {
    background: linear-gradient(180deg, var(--bg-top) 0%, var(--bg-top) 55%, var(--bg-bottom) 100%);
    position: relative;
    font-family: "Cormorant Garamond", serif;
  }

  /* Neck label */
  .neck-label {
    position: absolute; left: 420px; top: 60px; width: 360px; height: 170px;
    background: var(--sage);
    border-top: 14px solid var(--paper);
    border-bottom: 14px solid var(--paper);
    box-shadow: 0 -26px 0 -12px var(--sage), 0 26px 0 -12px var(--sage);
    text-align: center; color: var(--paper);
  }
  .neck-label .brand { font-family: "Great Vibes", cursive; font-size: 52px; line-height: 1; margin-top: 12px; }
  .neck-label .batch { font-family: "Cinzel", serif; font-weight: 600; font-size: 15px; letter-spacing: 4px; margin-top: 2px; }
  .neck-label .spirit { font-family: "Oswald", sans-serif; font-weight: 500; font-size: 46px; line-height: 1.1; }

  /* Front label */
  .front-label {
    position: absolute; left: 110px; top: 290px; width: 460px; height: 640px;
    background: var(--paper);
    border: 10px solid var(--sage);
    outline: 4px solid var(--paper);
    border-radius: 70px;
    box-shadow: 0 0 0 14px var(--sage);
    overflow: hidden;
  }
  .front-label .filigree { position: absolute; width: 220px; height: 300px; }
  .front-label .f-tl { left: 0; top: 0;
    background: radial-gradient(ellipse 85% 85% at 10% 15%, rgba(var(--filigree), .6) 0%, rgba(var(--filigree), .3) 45%, rgba(var(--filigree), 0) 75%); }
  .front-label .f-tr { right: 0; top: 0;
    background: radial-gradient(ellipse 85% 85% at 90% 15%, rgba(var(--filigree), .6) 0%, rgba(var(--filigree), .3) 45%, rgba(var(--filigree), 0) 75%); }
  .front-label .f-bl { left: 0; bottom: 0;
    background: radial-gradient(ellipse 85% 85% at 10% 85%, rgba(var(--filigree), .6) 0%, rgba(var(--filigree), .3) 45%, rgba(var(--filigree), 0) 75%); }
  .front-label .f-br { right: 0; bottom: 0;
    background: radial-gradient(ellipse 85% 85% at 90% 85%, rgba(var(--filigree), .6) 0%, rgba(var(--filigree), .3) 45%, rgba(var(--filigree), 0) 75%); }
  .emblem {
    position: absolute; left: 50%; top: 22px; transform: translateX(-50%);
    width: 92px; height: 92px; border-radius: 50%;
    background: var(--emblem); border: 4px solid var(--sage);
    display: flex; align-items: center; justify-content: center;
    font-family: "Cormorant Garamond", serif; font-size: 13px; color: var(--paper);
  }
  .botanical {
    position: absolute; left: 50%; top: 135px; transform: translateX(-50%);
    width: 170px; height: 320px;
    background: radial-gradient(ellipse 50% 50% at 50% 50%, rgba(143,174,152,.45) 0%, rgba(143,174,152,.2) 55%, rgba(143,174,152,0) 100%);
  }
  .front-label .text { position: absolute; left: 0; right: 0; text-align: center; }
  .front-label .brand { top: 222px; font-family: "Great Vibes", cursive; font-size: 76px; color: var(--ink); line-height: 1; }
  .front-label .batch { top: 318px; font-family: "Cinzel", serif; font-weight: 600; font-size: 22px; letter-spacing: 5px; color: var(--ink); }
  .front-label .spirit { top: 395px; font-family: "Oswald", sans-serif; font-weight: 500; font-size: 104px; line-height: 1; color: var(--sage-text); }
  .front-label .origin { top: 522px; font-size: 15px; letter-spacing: 1px; color: var(--ink); }
  .front-label .volume { top: 545px; font-size: 30px; color: var(--ink); font-variant-numeric: lining-nums; }

  /* Recipe label */
  .recipe-label {
    position: absolute; left: 650px; top: 400px; width: 440px; height: 520px;
    background: var(--sage);
    border-radius: 90px 90px 60px 60px;
    box-shadow: inset 0 0 0 8px var(--sage), inset 0 0 0 11px var(--paper);
    overflow: hidden; color: var(--paper); text-align: center;
  }
  .recipe-label .filigree { position: absolute; width: 240px; height: 300px; }
  .recipe-label .f-tr { right: 0; top: 0;
    background: radial-gradient(ellipse 80% 75% at 95% 10%, rgba(var(--filigree-green), .7) 0%, rgba(var(--filigree-green), .3) 45%, rgba(var(--filigree-green), 0) 75%); }
  .recipe-label .f-l { left: 0; top: 60px;
    background: radial-gradient(ellipse 50% 80% at 5% 45%, rgba(var(--filigree-green), .65) 0%, rgba(var(--filigree-green), .25) 45%, rgba(var(--filigree-green), 0) 75%); }
  .recipe-label .f-br { right: 0; bottom: 0;
    background: radial-gradient(ellipse 55% 90% at 95% 80%, rgba(var(--filigree-green), .7) 0%, rgba(var(--filigree-green), .3) 45%, rgba(var(--filigree-green), 0) 75%); }
  .recipe-label .f-bl { left: 0; bottom: 0;
    background: radial-gradient(ellipse 80% 50% at 15% 95%, rgba(var(--filigree-green), .7) 0%, rgba(var(--filigree-green), .3) 45%, rgba(var(--filigree-green), 0) 75%); }
  .recipe-title {
    position: relative; margin-top: 60px; font-weight: normal;
    font-family: "Great Vibes", cursive; font-size: 68px; line-height: 1;
  }
  .recipe-rule { position: relative; width: 150px; height: 3px; background: var(--paper); margin: 6px auto 20px; border-radius: 2px; }
  .recipe-text {
    position: relative; width: 300px; margin: 0 auto;
    font-family: "Pompiere", sans-serif; font-size: 30px; line-height: 1.15; color: #fbfbfb;
  }
  .recipe-proof {
    position: relative; margin-top: 22px;
    font-family: "Arimo", sans-serif; font-size: 20px; line-height: 1.25; color: var(--ink);
  }
</style>
</head>
<body>
  <section class="neck-label">
    <div class="brand">Wanderlark</div>
    <div class="batch">SMALL BATCH</div>
    <div class="spirit">GIN</div>
  </section>

  <section class="front-label">
    <div class="filigree f-tl" role="img" aria-label="Grey filigree scroll ornament"></div>
    <div class="filigree f-tr" role="img" aria-label="Grey filigree scroll ornament"></div>
    <div class="filigree f-bl" role="img" aria-label="Grey filigree scroll ornament"></div>
    <div class="filigree f-br" role="img" aria-label="Grey filigree scroll ornament"></div>
    <div class="botanical" role="img" aria-label="Engraved sprig of flowering manuka"></div>
    <div class="emblem">Wanderlark</div>
    <div class="text brand">Wanderlark</div>
    <div class="text batch">SMALL BATCH</div>
    <div class="text spirit">GIN</div>
    <div class="text origin">NEWZELAND</div>
    <div class="text volume">500ML</div>
  </section>

  <section class="recipe-label">
    <div class="filigree f-tr" role="img" aria-label="Green filigree scroll ornament"></div>
    <div class="filigree f-l" role="img" aria-label="Green filigree scroll ornament"></div>
    <div class="filigree f-br" role="img" aria-label="Green filigree scroll ornament"></div>
    <div class="filigree f-bl" role="img" aria-label="Green filigree scroll ornament"></div>
    <h2 class="recipe-title">Recipe</h2>
    <div class="recipe-rule"></div>
    <p class="recipe-text">A Classicaly inspired Gin with Developed Citrus notes from the Manuka Berries from Rowan's Mates, best with a Equal Mix of some Fancy Tonic</p>
    <p class="recipe-proof">84 PROOF<br>42% Alc. by vol.</p>
  </section>
</body>
</html>
```